Project Managers Business card design

We need business cards for our Project Managers based in Sydney for our business name Korbet Pty Ltd. We project manage property improvements and infrastructure Assets. We provide asset owners Project Management services from original concept, management of architectural and engineering designs, call and select construction tenders, and manage the Asset operational life cycle to conclusion and removal. We are experienced in feasibility studies, risk assessments, quality control, safety control, environmental analysis. We are specialist in Aged Care and Child Care Services. We can provide asset reviewing checklists, asset inspections, contract cost and contract assessments, dispute resolution services and articles and books on safely working and living in environments subject to analysis. the design colours should be queensland marone and NSW sky blue.

Industry/Entity Type

Construction

Contact Information for Business Card

Gavin Trelowe (Mb 0412 847 391), Dennis Marquay (Mb 0438 216 074), Luke Benhadda,(Mb 0421 963 158)
E: all business cards: korbet@fernmail.example
Office phone number (02) 9482 3165
Address
Level 1 Halyard House
47 Wexford Lane, Parramatta
Web: projectmanagers@worksleadsbykorbet.example (to be checked on Printlyne web draft)

```html
<!DOCTYPE html>
<html lang="en">
<head>
<meta charset="utf-8">
<title>Korbet Pty Ltd – Business Card</title>
<link rel="stylesheet" href="https://fonts.googleapis.com/css2?family=Cinzel:wght@700&family=Ubuntu:ital,wght@0,300;0,400;1,400;1,700&display=swap">
<style>
  :root {
    --backdrop: #d8dde0;
    --card: #f4f4f2;
    --maroon: #73182c;
    --sky: #7cc1e4;
    --ink: #3a0c17;
    --on-dark: #f1e9eb;
  }
  * { margin: 0; padding: 0; box-sizing: border-box; }
  html, body { width: 1200px; height: 1000px; overflow: hidden; }
  body { background: var(--backdrop); position: relative; font-family: "Ubuntu", sans-serif; }

  .card {
    position: absolute; left: 250px; width: 700px; height: 400px;
    background: var(--card); overflow: hidden;
    box-shadow: 0 6px 18px rgba(0,0,0,0.18);
  }
  .card--front { top: 60px; }
  .card--back { top: 540px; }
  .card__shapes { position: absolute; inset: 0; }
  .card__shapes .band { fill: var(--maroon); }
  .card__shapes .stripe { fill: var(--sky); }

  .company-name {
    position: absolute; left: 0; width: 100%; text-align: center;
    font-family: "Cinzel", serif; font-weight: 700; color: var(--ink);
    letter-spacing: 1px;
  }
  .card--front .company-name { top: 160px; font-size: 56px; }
  .card--back .company-name { top: 14px; font-size: 32px; }

  .person { position: absolute; left: 250px; top: 92px; width: 255px; text-align: center; color: var(--ink); }
  .person__name { font-style: italic; font-weight: 700; font-size: 27px; }
  .person__role { font-style: italic; font-size: 16px; margin-top: 2px; }

  .contact {
    position: absolute; color: var(--on-dark); text-align: center;
    font-weight: 300; font-size: 18px; line-height: 26px;
  }
  .contact--lines { left: 10px; top: 212px; width: 480px; }
  .contact--address { left: 0; top: 350px; width: 700px; font-size: 23px; font-weight: 400; }
  .contact__gap { display: inline-block; width: 28px; }
</style>
</head>
<body>

  <section class="card card--front" aria-label="Card front">
    <svg class="card__shapes" width="700" height="400" viewBox="0 0 700 400">
      <rect class="band" x="0" y="0" width="430" height="70"/>
      <rect class="stripe" x="444" y="0" width="20" height="70"/>
      <rect class="stripe" x="476" y="0" width="20" height="70"/>
      <rect class="band" x="510" y="0" width="190" height="70"/>
      <rect class="band" x="0" y="330" width="300" height="70"/>
      <rect class="stripe" x="314" y="300" width="20" height="100"/>
      <rect class="stripe" x="346" y="300" width="20" height="100"/>
      <rect class="band" x="380" y="330" width="320" height="70"/>
    </svg>
    <h1 class="company-name">Korbet Pty Ltd</h1>
  </section>

  <section class="card card--back" aria-label="Card back">
    <svg class="card__shapes" width="700" height="400" viewBox="0 0 700 400">
      <rect class="stripe" x="0" y="70" width="250" height="105"/>
      <rect class="stripe" x="505" y="175" width="195" height="95"/>
      <polygon class="band" points="0,195 490,195 490,290 700,290 700,400 0,400"/>
    </svg>
    <h2 class="company-name">Korbet Pty Ltd</h2>
    <div class="person">
      <p class="person__name">Luke Benhadda</p>
      <p class="person__role">Project Manager</p>
    </div>
    <div class="contact contact--lines">
      <p>M : 0421 963 158<span class="contact__gap"></span>O : (02) 9482 3165</p>
      <p>E : korbet@fernmail.example</p>
      <p>W : projectmanagers@worksleadsbykorbet.example</p>
      <p>(to be checked on Printlyne web draft)</p>
    </div>
    <p class="contact contact--address">Level 1 Halyard House 47 Wexford Lane, Parramatta</p>
  </section>

</body>
</html>
```